Website for an interior designer

We need a new website for Clara Beth Holloway whose new business name is Clara Beth Holloway Interiors. She is a residential interior designer with a mix of modern and contemporary tastes. We are in the process of overhauling her website which is +15 years old and not an accurate reflection of her tastes. The uploaded photos are from some of the houses she has done as well as her logo(s). We would need a section for "About Us" that would have a paragraph of text and bullets showing services and a gallery for photos (~12 total, more to come). A contract page would be optional. The client likes the feel/look of this website: https://www.pondrickstudio.example/ but doesn't want to copy it exactly.

Target Market(s)

Upscale home owners

Industry/Entity Type

Interior Design

Coding

Coded - Design and coding required

Number of Pages Required

4 page

Colors

Designer to choose only greyscale colors for use in the design.

Requirements
Must have
• Home page, about us page, gallery page, contact us page.

```html
<!DOCTYPE html>
<html lang="en">
<head>
<meta charset="utf-8">
<title>Clara Beth Holloway Interiors</title>
<link rel="stylesheet" href="https://fonts.googleapis.com/css2?family=Cinzel:wght@400&family=Open+Sans:wght@400;600&display=swap">
<style>
:root{
  --ink:#2b2b2b;
  --text:#6b6b6b;
  --muted:#a8a4a3;
  --panel:#c2bcbb;
  --line:#b9b9b9;
  --footer:#868890;
  --white:#ffffff;
}
*{margin:0;padding:0;box-sizing:border-box}
html,body{width:1200px;height:3081px;overflow:hidden;background:var(--white)}
body{position:relative;font-family:"Open Sans",Arial,sans-serif;color:var(--text)}
.abs{position:absolute}
.serif{font-family:"Cinzel",Georgia,serif;font-weight:400}

/* header */
.contact-line{left:110px;font-size:16px;color:var(--ink);display:flex;align-items:center;gap:10px}
.brand-name{left:0;width:1200px;top:98px;text-align:center;font-size:26px;color:var(--ink)}
.search{left:1005px;top:99px;font-size:17px;color:var(--ink);display:flex;align-items:center;gap:10px}

.nav{top:191px;left:0;width:1200px;display:flex;justify-content:center;gap:46px;font-size:18px;color:var(--ink)}
.nav a{color:inherit;text-decoration:none;display:flex;align-items:center;gap:22px}
.nav a.current{color:var(--muted)}
.nav .dot{width:10px;height:10px;background:var(--ink);transform:rotate(45deg)}
.nav a.current .dot{background:var(--muted)}

/* hero */
.hero-photo{left:111px;top:243px;width:624px;height:480px;background:linear-gradient(160deg,#ecebe6,#cfc7b9 60%,#8d7d6a)}
.hero-panel{left:735px;top:243px;width:351px;height:480px;background:var(--panel)}
.hero-title{left:814px;top:276px;width:260px;font-size:38px;line-height:54px;color:var(--white)}
.hero-text{left:814px;top:448px;width:240px;font-size:19px;line-height:30px;color:var(--white)}
.hero-btn{left:812px;top:596px;width:238px;height:51px;border:2px solid var(--white);color:var(--white);font-size:17px;font-weight:600;display:flex;align-items:center;justify-content:center}
.diamond{background:var(--white);transform:rotate(45deg)}

/* sections */
.center{left:0;width:1200px;text-align:center}
.label{font-size:26px;color:var(--muted)}
.heading{font-size:42px;line-height:52px;color:#8c8c8c}
.para{left:245px;width:710px;text-align:center;font-size:15.5px;line-height:33px}
.btn{border:2px solid var(--line);color:var(--muted);font-size:17px;font-weight:600;display:flex;align-items:center;justify-content:center;letter-spacing:.5px}

.services{left:111px;width:380px;list-style:none}
.services li{position:absolute;left:0;width:370px;padding-left:29px;font-size:14px;line-height:23px;color:var(--text)}
.services svg{position:absolute;left:0;top:5px}

.tile{position:absolute}

/* footer */
.footer{left:0;top:2807px;width:1200px;height:274px;background:var(--footer)}
.foot-line{left:0;width:1200px;text-align:center;color:var(--white);font-size:17px}
.foot-line span{margin:0 16px}
.social{top:3018px;left:552px;display:flex;gap:10px}
.social i{display:block;width:23px;height:23px;background:var(--white);border-radius:3px}
</style>
</head>
<body>

<header>
  <div class="abs contact-line" style="top:62px">
    <svg width="13" height="13" viewBox="0 0 24 24"><path fill="#9a9a9a" d="M6.6 10.8a15 15 0 0 0 6.6 6.6l2.2-2.2c.3-.3.7-.4 1-.2 1.1.4 2.3.6 3.6.6.6 0 1 .4 1 1V20c0 .6-.4 1-1 1A17 17 0 0 1 3 4c0-.6.4-1 1-1h3.5c.6 0 1 .4 1 1 0 1.3.2 2.5.6 3.6.1.3 0 .7-.2 1z"/></svg>
    888-888-8888
  </div>
  <div class="abs contact-line" style="top:95px">
    <svg width="16" height="12" viewBox="0 0 16 12"><rect width="16" height="12" rx="1" fill="#9a9a9a"/><path d="M0 1l8 6 8-6" stroke="#fff" stroke-width="1.4" fill="none"/></svg>
    sample@sample.com
  </div>

  <div class="abs brand-name serif">CLARA BETH HOLLOWAY INTERIORS</div>

  <div class="abs search">
    <svg width="16" height="16" viewBox="0 0 16 16"><circle cx="6.5" cy="6.5" r="5" stroke="#9a9a9a" stroke-width="2" fill="none"/><path d="M10 10l4.5 4.5" stroke="#9a9a9a" stroke-width="2"/></svg>
    Search
  </div>

  <nav class="abs nav">
    <a class="current" href="#"><span class="dot"></span>HOME</a>
    <a href="#"><span class="dot"></span>ABOUT US</a>
    <a href="#"><span class="dot"></span>GALLERY</a>
    <a href="#"><span class="dot"></span>CONTACT US</a>
  </nav>
</header>

<section>
  <div class="abs hero-photo" role="img" aria-label="Bright living room with white sofas, glass coffee table and tall black-framed windows"></div>
  <div class="abs hero-panel"></div>
  <div class="abs hero-title serif">CLARA BETH<br>HOLLOWAY<br>INTERIORS</div>
  <p class="abs hero-text">Clara Beth Holloway has extensive experience in all aspects of interior design.</p>
  <div class="abs hero-btn">NEW PROJECT REQUEST</div>
  <div class="abs diamond" style="left:681px;top:429px;width:108px;height:108px"></div>
</section>

<section>
  <div class="abs center label serif" style="top:790px">ABOUT US</div>
  <h2 class="abs center heading serif" style="top:830px">WELCOME TO CLARA BETH<br>HOLLOWAY INTERIORS</h2>
  <p class="abs para" style="top:958px">Clara Beth Holloway has extensive experience in all aspects of interior design. She has worked on a wide array of residential and commercial projects in her hometown of Houston and across the United States. Clara Beth’s taste can best be described as a sophisticated blend of modern and traditional styles that combine to create a clean, timeless space.</p>
  <div class="abs btn" style="left:506px;top:1127px;width:189px;height:59px">ABOUT US</div>
</section>

<section>
  <div class="abs label serif" style="left:105px;top:1255px">SERVICES</div>
  <h2 class="abs heading serif" style="left:105px;top:1294px">WHAT WE DO</h2>
  <ul class="abs services" style="top:0">
    <li style="top:1366px"><svg width="14" height="14" viewBox="0 0 14 14"><circle cx="7" cy="7" r="7" fill="#a9a9a9"/><path d="M4 7.2l2 2 4-4" stroke="#fff" stroke-width="1.6" fill="none"/></svg>Concept Origination and Project Management</li>
    <li style="top:1412px"><svg width="14" height="14" viewBox="0 0 14 14"><circle cx="7" cy="7" r="7" fill="#a9a9a9"/><path d="M4 7.2l2 2 4-4" stroke="#fff" stroke-width="1.6" fill="none"/></svg>Review of Proposed Plans for New Construction and Remodels</li>
    <li style="top:1482px"><svg width="14" height="14" viewBox="0 0 14 14"><circle cx="7" cy="7" r="7" fill="#a9a9a9"/><path d="M4 7.2l2 2 4-4" stroke="#fff" stroke-width="1.6" fill="none"/></svg>Procurement of Furniture, Accents, Art, Fixtures and Fittings</li>
    <li style="top:1551px"><svg width="14" height="14" viewBox="0 0 14 14"><circle cx="7" cy="7" r="7" fill="#a9a9a9"/><path d="M4 7.2l2 2 4-4" stroke="#fff" stroke-width="1.6" fill="none"/></svg>Selection of Paints, Finishes and Construction Materials</li>
    <li style="top:1621px"><svg width="14" height="14" viewBox="0 0 14 14"><circle cx="7" cy="7" r="7" fill="#a9a9a9"/><path d="M4 7.2l2 2 4-4" stroke="#fff" stroke-width="1.6" fill="none"/></svg>Vendor Coordination and Recommendations</li>
    <li style="top:1667px"><svg width="14" height="14" viewBox="0 0 14 14"><circle cx="7" cy="7" r="7" fill="#a9a9a9"/><path d="M4 7.2l2 2 4-4" stroke="#fff" stroke-width="1.6" fill="none"/></svg>Home Staging, Styling and Editing</li>
  </ul>
  <div class="abs btn" style="left:111px;top:1724px;width:173px;height:60px">READ MORE</div>
  <div class="abs" role="img" aria-label="White kitchen with marble island, stainless range hood and grey cabinets" style="left:488px;top:1262px;width:601px;height:521px;background:linear-gradient(170deg,#eeeeec,#c9cbcb 55%,#6b5a4a)"></div>
</section>

<section>
  <div class="abs center label serif" style="top:1853px">GALLERY</div>
  <h2 class="abs center heading serif" style="top:1893px">OUR PROJECTS</h2>

  <div class="tile" role="img" aria-label="White curved staircase in bright entry hall" style="left:111px;top:1995px;width:238px;height:351px;background:linear-gradient(180deg,#eeeeeb,#d7d5cf 70%,#8a7866)"></div>
  <div class="tile" role="img" aria-label="Study with bookshelves, grey armchairs and fireplace" style="left:358px;top:1995px;width:238px;height:351px;background:linear-gradient(180deg,#6f7273,#9a9a96 55%,#bdb9b1)"></div>
  <div class="tile" role="img" aria-label="Staircase with colourful painted runner" style="left:604px;top:1995px;width:238px;height:351px;background:linear-gradient(160deg,#e8dfc8,#d98a4a 45%,#c85a86)"></div>
  <div class="tile" role="img" aria-label="Dining area with white table, chairs and brass pendant" style="left:851px;top:1995px;width:238px;height:351px;background:linear-gradient(180deg,#d9d6cf,#e6e6e4 55%,#5a4c42)"></div>

  <div class="tile" role="img" aria-label="Covered patio with outdoor seating" style="left:111px;top:2358px;width:238px;height:214px;background:linear-gradient(180deg,#e4e6e7,#8a6c5c 60%,#7a8a5a)"></div>
  <div class="tile" role="img" aria-label="White kitchen with marble island" style="left:358px;top:2358px;width:238px;height:214px;background:linear-gradient(170deg,#ededeb,#cacccc 60%,#6b5a4a)"></div>
  <div class="tile" role="img" aria-label="Living room with white sofas and tall windows" style="left:604px;top:2358px;width:238px;height:214px;background:linear-gradient(170deg,#eceae4,#cfc7b9 60%,#7d6d5c)"></div>
  <div class="tile" role="img" aria-label="Sitting room with curved blush sofa and framed artwork" style="left:851px;top:2358px;width:238px;height:214px;background:linear-gradient(170deg,#e2ddd9,#d7c8bd 60%,#c7b1a4)"></div>

  <div class="abs btn" style="left:514px;top:2625px;width:173px;height:60px">VIEW MORE</div>
</section>

<footer>
  <div class="abs footer"></div>
  <div class="abs diamond" style="left:558px;top:2762px;width:87px;height:87px;border:3px solid var(--footer)"></div>
  <div class="abs foot-line" style="top:2894px">Home<span>|</span>About us<span>|</span>Gallery<span>|</span>Contact us</div>
  <div class="abs foot-line" style="top:2937px">Cell: 888-888-8888<span>|</span>Email: sample@sample.com</div>
  <div class="abs foot-line" style="top:2970px">© 2020,&nbsp; Clara Beth Holloway Interiors.</div>
  <div class="abs social"><i></i><i></i><i></i></div>
</footer>

</body>
</html>
```